Card Design for my dog training business Rustpaw Obedience

Need a business card design for my dog training business with my new logo. Want the card to come off professional yet fun. Want it to be very eye catchy as well. I normally have these at vet clinics, pet stores, and groomers. so need it to look better than my competitors.
Target Market(s)
dog owners
Industry/Entity Type
Dog Training
Contact Information for Business Card
needs logo, my name and info
Font styles to use
Serif
Colors
0255a3
ffffff
ec1f27
000000
333333
fbfbfb
Requirements
Must have
- Rustpaw Obedience
- Hollis Brandt
- 415 903 2267
- info@rustpawobedience.example
- www.rustpawobedience.example

```html
<!DOCTYPE html>
<html lang="en">
<head>
<meta charset="utf-8">
<title>Rustpaw Obedience — Business Card</title>
<link href="https://fonts.googleapis.com/css2?family=EB+Garamond:ital,wght@1,400&family=Noto+Serif:wght@400&display=swap" rel="stylesheet">
<style>
  :root {
    --backdrop: #3a3a3a;
    --card: #1f1f21;
    --silver: #c9c9cb;
    --muted: #a8a8ab;
    --brand-blue: #0255a3;
    --name-blue: #1f8fe0;
    --brand-red: #ec1f27;
    --white: #ffffff;
  }
  * { margin: 0; padding: 0; box-sizing: border-box; }
  html, body {
    width: 799px; height: 1200px; overflow: hidden;
    background: var(--backdrop);
  }
  .sheet {
    position: relative; width: 799px; height: 1200px;
  }
  .card {
    position: absolute; left: 80px; width: 640px; height: 366px;
    background: var(--card);
    overflow: hidden;
    box-shadow: 0 10px 30px rgba(0,0,0,0.45);
  }
  .card--front { top: 117px; }
  .card--back { top: 717px; }

  .wordmark {
    position: absolute;
    display: flex; align-items: center; gap: 12px;
    font-family: "Noto Serif", serif; font-weight: 400;
    color: var(--silver);
  }
  .wordmark__dot {
    width: 16px; height: 16px; border-radius: 50%;
    background: var(--silver); flex: none;
  }
  .card--front .wordmark {
    left: 0; right: 0; top: 140px; justify-content: center;
    font-size: 34px; letter-spacing: 1px;
  }
  .card--front .tagline {
    position: absolute; left: 0; right: 0; top: 262px;
    text-align: center;
    font-family: "EB Garamond", serif; font-style: italic;
    font-size: 18px; color: var(--muted);
  }

  .card--back .wordmark {
    left: 44px; top: 130px; width: 250px;
    font-size: 24px; line-height: 1.2;
  }
  .contact {
    position: absolute; left: 330px; top: 118px;
    font-family: "Noto Serif", serif;
  }
  .contact__name {
    font-size: 24px; color: var(--name-blue); line-height: 1.2;
  }
  .contact__role {
    font-size: 13px; color: var(--muted); margin-bottom: 12px;
  }
  .contact__row {
    display: flex; align-items: center; gap: 10px;
    font-size: 14px; color: var(--silver); line-height: 24px;
  }
  .contact__row svg { width: 13px; height: 13px; flex: none; }

  .stripe-red {
    position: absolute; left: 0; top: 300px; width: 236px; height: 11px;
    background: var(--brand-red);
  }
  .band-blue {
    position: absolute; left: 224px; right: 0; top: 294px; bottom: 0;
    background: var(--brand-blue);
    border-top-left-radius: 30px;
    display: flex; align-items: center; justify-content: center;
    font-family: "EB Garamond", serif; font-style: italic;
    font-size: 17px; color: var(--white);
  }
</style>
</head>
<body>
<main class="sheet">
  <section class="card card--front">
    <div class="wordmark"><span class="wordmark__dot"></span>Rustpaw Obedience</div>
    <p class="tagline">“Training dogs across Texas one dog at a time. ”</p>
  </section>

  <section class="card card--back">
    <div class="wordmark"><span class="wordmark__dot"></span>Rustpaw Obedience</div>
    <div class="contact">
      <p class="contact__name">Hollis Brandt</p>
      <p class="contact__role">Dog Trainer</p>
      <p class="contact__row">
        <svg viewBox="0 0 16 16" aria-hidden="true"><path fill="#1f8fe0" d="M3 1h3l1.5 4-2 1.2a9 9 0 0 0 4.3 4.3l1.2-2 4 1.5v3a2 2 0 0 1-2 2A13 13 0 0 1 1 3a2 2 0 0 1 2-2z"/></svg>
        415 903 2267
      </p>
      <p class="contact__row">
        <svg viewBox="0 0 16 16" aria-hidden="true"><rect x="1" y="3" width="14" height="10" rx="1" fill="#1f8fe0"/><path d="M1.5 3.5 8 9l6.5-5.5" fill="none" stroke="#1f1f21" stroke-width="1.3"/></svg>
        info@rustpawobedience.example
      </p>
      <p class="contact__row">
        <svg viewBox="0 0 16 16" aria-hidden="true"><circle cx="8" cy="8" r="7" fill="#1f8fe0"/><path d="M1 8h14M8 1c-3 3.5-3 10.5 0 14M8 1c3 3.5 3 10.5 0 14" fill="none" stroke="#1f1f21" stroke-width="1"/></svg>
        www.rustpawobedience.example
      </p>
    </div>
    <div class="stripe-red"></div>
    <div class="band-blue">“Training dogs across Texas one dog at a time. ”</div>
  </section>
</main>
</body>
</html>
```